Law Firm
To All Designers:
New e-mail address for the project is daniel@rvestlegal.net.
Thanks. I love all the designs.
P.S. I like the orange on the one side of the card as opposed to black.
@ph - New drafts #161 & #162 in lieu of 145 & 146 are submitted, Can you please check & provide feedback in private message.
Thanks
draft #145 and #146 Drafts came out black and I cannot see them (look like negatives). Please resubmit. Thanks.
Please DO NOT PUT "Gavels", "Scales of Justice" "Court Buildings", etc. on the card. I DO NOT WANT IT.
Thanks.
draft #130 Card looks a lot better. Can I see it with the dot at the end of the big line through the card a little smaller (but that is the look I was going for) and can I see some color (black, orange and/or grey) below that line where the address, phone and e-mail appear? Also, can I see with just the "m" and the line part of the logo on the other side? Thanks.
draft #125 and #126 Looks better. I didn't like the "watermark" "m" in my logo being sideways on the card (it didn't look like an "m" anymore to me that way), but Ido like it on the stationary and envelope. Can I see the card with the same orange on the one side with the orange line under the "m" in my logo at the bottom of the card then the address, telephone and e-mail below it? Thanks.
To all designers,
Can I start seeing letterhead, envelopes, fax covers and e-mail signatures too! I look forward to seeing the designs!
draft #49 I like the line under my name like in the logo. Can I see with orange on the other side of the card?
drafts #101, #102, #103 and #104 I would like to see with orange on the other side of the card rather than black
I like the use of the whites and oranges with black accents. So not too much black. I also like orange with the logo (either with the text or just the script "m") on one side of the card. Thanks for all the great designs.
draft #35 I like the use of the logo at the bottom of the card. But "no "scales of justice", "court buildings" or "gavels", etc. was not something I wanted on the card, it was just an instruction to the designers that although I am a lawyer, I do not want to use these symbols.
draft #31 and #32 Maybe you could use the orange line under the script "m" under the logo for the "white space"?
draft #31 and #32 Like the use of the colors in the card and the "watermark" logo on the stationary. However, there is too much "white space" on the right side of the card. Other drafts did better job with "white space". I would also like to maybe see the "watermark" logo used in the card as well.

```html
<!DOCTYPE html>
<html lang="en">
<head>
<meta charset="utf-8">
<title>Daniel R. Vest P.C. – Business Card</title>
<link rel="stylesheet" href="https://fonts.googleapis.com/css2?family=Crimson+Text:wght@400;700&display=swap">
<style>
  :root {
    --backdrop: #2b2b2d;
    --card-black: #1c1c1e;
    --card-white: #f7f7f5;
    --brand-orange: #e0622a;
    --ink: #1d1d1f;
    --ink-soft: #3a3a3c;
    --rule-white: #fbeee6;
  }
  * { box-sizing: border-box; margin: 0; padding: 0; }
  html, body {
    width: 1200px; height: 901px; overflow: hidden;
    background: var(--backdrop);
  }
  .canvas { position: relative; width: 1200px; height: 901px; }

  .card {
    position: absolute; width: 630px; height: 360px;
    border-radius: 4px; overflow: hidden;
    box-shadow: 0 10px 30px rgba(0,0,0,.45);
  }

  /* Back side */
  .card-back {
    left: 90px; top: 70px;
    background: var(--card-black);
    display: flex; align-items: center; justify-content: center;
  }
  .card-back .firm-name {
    font-family: "Crimson Text", serif; font-weight: 400;
    font-size: 36px; color: var(--card-white);
  }

  /* Front side */
  .card-front { left: 480px; top: 470px; background: var(--card-white); }
  .card-front .band { position: absolute; inset: 0; }

  .brand {
    position: absolute; left: 0; right: 0; top: 58px; text-align: center;
    font-family: "Crimson Text", serif; color: var(--ink);
  }
  .brand .firm-name { font-size: 40px; font-weight: 400; }
  .brand .tagline {
    margin-top: 2px; font-size: 20px; font-weight: 400;
    letter-spacing: 1px; color: var(--ink-soft);
  }

  .holder {
    position: absolute; left: 60px; top: 242px; width: 240px; text-align: right;
    font-family: "Crimson Text", serif; color: var(--ink);
  }
  .holder .name { font-size: 26px; font-weight: 700; }
  .holder .role { font-size: 19px; color: var(--ink-soft); }

  .divider {
    position: absolute; left: 322px; top: 200px; width: 2px; height: 128px;
    background: var(--rule-white);
  }

  .contact {
    position: absolute; left: 340px; top: 200px;
    font-family: "Crimson Text", serif; font-size: 17px; line-height: 23px;
    color: var(--ink); list-style: none;
  }
  .contact li { display: flex; align-items: center; gap: 6px; }
  .contact svg { width: 16px; height: 16px; flex: none; }
</style>
</head>
<body>
<main class="canvas">

  <section class="card card-back" aria-label="Card back">
    <span class="firm-name">Daniel R. Vest P.C.</span>
  </section>

  <section class="card card-front" aria-label="Card front">
    <svg class="band" viewBox="0 0 630 360" preserveAspectRatio="none" aria-hidden="true">
      <path d="M0 214 C 160 150, 330 168, 630 150 L630 360 L0 360 Z" fill="var(--ink)"/>
      <path d="M0 222 C 160 160, 330 178, 630 162 L630 360 L0 360 Z" fill="var(--brand-orange)"/>
    </svg>

    <header class="brand">
      <div class="firm-name">Daniel R. Vest P.C.</div>
      <div class="tagline">Legal Consulting</div>
    </header>

    <div class="holder">
      <div class="name">Daniel R. Vest</div>
      <div class="role">Principal</div>
    </div>

    <div class="divider"></div>

    <ul class="contact">
      <li>18 Harlow Lane</li>
      <li>Brookfield, NY 10598</li>
      <li>
        <svg viewBox="0 0 16 16" aria-hidden="true"><circle cx="8" cy="8" r="8" fill="var(--ink)"/><path d="M5 4.5c.6-.5 1.2-.3 1.5.3l.5 1c.2.4 0 .8-.3 1l-.4.3c.4.9 1.1 1.6 2 2l.3-.4c.3-.3.7-.4 1-.2l1 .5c.6.3.7 1 .2 1.5-.9.9-2.3.8-4-.6S4.1 5.4 5 4.5z" fill="var(--card-white)"/></svg>
        (917) 555-0143
      </li>
      <li>
        <svg viewBox="0 0 16 16" aria-hidden="true"><circle cx="8" cy="8" r="8" fill="var(--ink)"/><rect x="4" y="5" width="8" height="6" rx="1" fill="var(--card-white)"/><path d="M4.3 5.4 8 8.4l3.7-3" stroke="var(--ink)" stroke-width="1" fill="none"/></svg>
        daniel@rvestlegal.net
      </li>
    </ul>
  </section>

</main>
</body>
</html>
```